Need a business card portraying store logo and up and coming business of quilt fabrics, apparel fabrics, notions and buttons. Our business name is Cherished Thread and Such. Am attaching logo. The design should communicate a growing business and warm atmosphere. Would like address and store hours and contact info displayed on card. Mon - Fri 9:30 to 5:00, Saturday 9:30 to 1:00. Address 238 W Elm Ave, Newton, KS 67392 email: cherishedthreadandsuch@mailbarn.net. Phone and fax 316-555-2847. After hours contact # 620-555-3916 Also like vintage sewing machines and dress forms if it works to incorporate fine, if not thats ok too.

```html
<!DOCTYPE html>
<html lang="en">
<head>
<meta charset="utf-8">
<title>Cherished Thread and Such – Business Card</title>
<link rel="stylesheet" href="https://fonts.googleapis.com/css2?family=Ubuntu:wght@400;500&display=swap">
<style>
  :root {
    --backdrop: #ecebe8;
    --card-red: #8e1b2a;
    --card-red-soft: #9c2636;
    --card-white: #ffffff;
    --ink-dark: #1f1f1f;
    --ink-light: #ffffff;
    --divider: #d9a0a8;
    --button-red: #b3202f;
  }
  * { box-sizing: border-box; margin: 0; padding: 0; }
  html, body {
    width: 1200px;
    height: 784px;
    overflow: hidden;
    background: var(--backdrop);
    font-family: "Ubuntu", Arial, sans-serif;
  }
  .canvas {
    position: relative;
    width: 1200px;
    height: 784px;
  }
  .card {
    position: absolute;
    top: 238px;
    width: 540px;
    height: 309px;
    overflow: hidden;
    box-shadow: 0 6px 18px rgba(0,0,0,0.15);
  }
  .card--front { left: 40px; background: var(--card-red); }
  .card--back { left: 620px; background: var(--card-white); }

  .decor {
    position: absolute;
    border-radius: 40px;
    background: linear-gradient(180deg, var(--card-red-soft), var(--card-red));
  }
  .decor--dress-form { left: 20px; top: 30px; width: 90px; height: 260px; }
  .decor--sewing-machine { left: 360px; top: 50px; width: 160px; height: 110px; }

  .brand {
    position: absolute;
    display: flex;
    align-items: center;
    gap: 14px;
  }
  .brand__dot {
    flex: none;
    width: 54px;
    height: 54px;
    border-radius: 50%;
  }
  .brand__name {
    font-size: 24px;
    font-weight: 400;
    letter-spacing: 0.2px;
    white-space: nowrap;
  }
  .card--front .brand { left: 80px; top: 108px; }
  .card--front .brand__dot { background: var(--card-white); }
  .card--front .brand__name { color: var(--ink-light); }

  .card--back .brand { left: 32px; top: 50px; }
  .card--back .brand__dot { background: var(--button-red); }
  .card--back .brand__name { color: var(--card-red); }

  .card__shape { position: absolute; inset: 0; }

  .hours {
    position: absolute;
    left: 30px;
    top: 238px;
    color: var(--ink-light);
    font-size: 17px;
    line-height: 1.3;
  }
  .info-divider {
    position: absolute;
    left: 238px;
    top: 190px;
    width: 1px;
    height: 100px;
    background: var(--divider);
  }
  .contact {
    position: absolute;
    left: 250px;
    top: 188px;
    list-style: none;
    color: var(--ink-light);
    font-size: 12px;
    line-height: 1.45;
  }
</style>
</head>
<body>
<main class="canvas">

  <section class="card card--front" aria-label="Card front">
    <div class="decor decor--dress-form" role="img" aria-label="Faint dress form illustration"></div>
    <div class="decor decor--sewing-machine" role="img" aria-label="Faint vintage sewing machine illustration"></div>
    <div class="brand">
      <span class="brand__dot"></span>
      <span class="brand__name">Cherished Thread and Such</span>
    </div>
  </section>

  <section class="card card--back" aria-label="Card back">
    <svg class="card__shape" viewBox="0 0 540 309" width="540" height="309" aria-hidden="true">
      <path d="M0,309 L0,225 C120,215 230,175 330,130 C420,90 490,50 540,10 L540,309 Z" fill="var(--card-red)"/>
      <path d="M405,90 C460,64 505,36 536,0" fill="none" stroke="var(--ink-dark)" stroke-width="5" stroke-linecap="round"/>
    </svg>
    <div class="brand">
      <span class="brand__dot"></span>
      <span class="brand__name">Cherished Thread and Such</span>
    </div>
    <p class="hours">Mon - Fri 9:30 to 5:00<br>Saturday 9:30 to 1:00</p>
    <span class="info-divider"></span>
    <ul class="contact">
      <li>238 W Elm Ave, Newton, KS 67392</li>
      <li>email: cherishedthreadandsuch@mailbarn.net</li>
      <li>Phone and fax: 316-555-2847</li>
      <li>After hours contact : 620-555-3916</li>
    </ul>
  </section>

</main>
</body>
</html>
```